Loftvane.ca Your Canadian Source for all your mortgage needs.

I need to get a fresh look on my current website. It is not currently a Wordpress site and i need to build a whole new site that i can do my editing in using Wordpress.
I need it built in a mobile or responsive theme.
There will be a secured application page which is critical.
I have 3 books written so i want to be able to have advertising spaces for promoting them and a landing page ( I can build my own landing pages)
I need the frame work of a professional theme with easy editing capabilities.
I have my own LOGOs which i would continue to use. The current site can be reviewed at www.loftvane.ca.
The front page could have a young couple near a nice house, open to suggestions.
I don't need a blog post to update but if it was on the sides of the pages I could use it. Something like a "Latest News" section.
I would like to have a Main page, Application Page, Resource page, Contact page, Calculator Page, a questions and answer page. Theses can be populated with the current information or I can add latter.
I want the main page to be a mini sales page so I can link to Posts on First Time Home Buyers, Refinance Options, Second Home or New purchase options.
I provide mortgages for people across Canada so i want the Canadian Flag incorporated
I like the colors to work with the logo colors on the current site

Target Market(s)

Canadian Mortgage Clients

Font styles to use
Sans Serif

Colors
3277b5
cadf82

Requirements
Must have
• Must work in a Wordpress Theme
• Please see Project description for more details
Nice to have
• Space to add banner ads for my books. I have 3 books written

```html
<!DOCTYPE html>
<html lang="en">
<head>
<meta charset="utf-8">
<title>Loftvane.ca – Your Canadian Source for Mortgages</title>
<link rel="stylesheet" href="https://fonts.googleapis.com/css2?family=Open+Sans:wght@400;600;700;800&display=swap">
<style>
:root{
  --blue:#3277b5;
  --blue-dark:#1f5a92;
  --lime:#cadf82;
  --green:#56a532;
  --green-dark:#3f8a22;
  --ink:#2b2b2b;
  --muted:#6b6b6b;
  --strip:#1c1d1f;
  --footer:#2a2d31;
  --footer-deep:#1d1f22;
  --line:#e3e3e3;
  --white:#ffffff;
}
*{box-sizing:border-box;margin:0;padding:0}
html,body{width:684px;height:1200px;overflow:hidden}
body{font-family:"Open Sans",Arial,sans-serif;color:var(--ink);background:var(--white);font-size:8px;line-height:1.4}
ul{list-style:none}

/* header */
.site-header{height:60px;display:flex;align-items:center;padding:0 24px;position:relative;border-bottom:1px solid var(--line)}
.brand{display:flex;align-items:center;gap:6px;font-weight:800;font-size:24px;color:var(--blue);letter-spacing:-0.5px}
.brand-mark{width:14px;height:14px;background:var(--green)}
.topbar{position:absolute;top:6px;right:24px;display:flex;align-items:center;gap:8px;font-size:11px;font-weight:600}
.flag{width:20px;height:12px;display:flex}
.flag span{flex:1;background:#d52b1e}
.flag span:nth-child(2){flex:2;background:#fff;border-top:1px solid #ddd;border-bottom:1px solid #ddd}
.phone-dot{width:14px;height:14px;border-radius:50%;background:var(--ink);display:flex;align-items:center;justify-content:center}
.main-nav{position:absolute;right:24px;bottom:8px;display:flex;gap:2px}
.main-nav a{font-size:8.5px;font-weight:700;color:var(--ink);text-decoration:none;padding:6px 8px;text-transform:uppercase}
.main-nav a.active{background:var(--green);color:#fff}

/* hero */
.hero{height:260px;position:relative;background:linear-gradient(160deg,#8d7c6a 0%,#b7a58d 35%,#6f8a4c 70%,#48612f 100%)}
.hero-caption{position:absolute;left:34px;top:70px;width:250px}
.hero-caption h1{font-size:14.5px;font-weight:700;color:#fff;line-height:1.25;text-shadow:0 1px 2px rgba(0,0,0,.5)}
.btn{display:inline-block;font-weight:700;color:#fff;text-decoration:none;border-radius:2px}
.btn-start{background:var(--blue);font-size:11px;padding:7px 14px;margin-top:12px}
.slider-dots{position:absolute;left:86px;bottom:10px;display:flex;gap:5px}
.slider-dots i{width:7px;height:7px;border-radius:50%;background:rgba(255,255,255,.5)}
.slider-dots i:first-child{background:#fff}

/* feature strip */
.features{height:85px;background:var(--strip);display:flex;padding:0 54px}
.feature{flex:1;display:flex;gap:10px;padding:16px 14px;color:#fff}
.feature.highlight{background:var(--green)}
.feature-icon{flex:none;width:28px;height:28px;border-radius:50%;background:var(--blue);display:flex;align-items:center;justify-content:center}
.feature.highlight .feature-icon{background:#fff}
.feature h3{font-size:11px;font-weight:700;line-height:1.2;margin-bottom:5px}
.feature p{font-size:6.5px;color:#cfcfcf}
.feature.highlight p{color:#eaf5df}

/* intro */
.intro{height:190px;display:flex;gap:24px;padding:14px 90px 0 74px}
.welcome{width:160px}
.section-title{font-size:11px;font-weight:800;text-transform:uppercase;color:var(--ink)}
.section-sub{font-size:8px;color:var(--blue);font-weight:600;border-bottom:1px solid var(--line);padding-bottom:4px;margin-bottom:6px}
.welcome p{font-size:7px;color:var(--muted);margin-bottom:8px}
.welcome .access{color:var(--blue);font-weight:700}
.btn-more{background:var(--ink);font-size:7px;padding:4px 10px}
.books{flex:1}
.book-row{display:flex;gap:14px;margin-top:4px}
.book{width:68px;text-align:center}
.book-cover{height:92px;border:1px solid var(--line)}
.book-cover.one{background:linear-gradient(#c8372d,#f0c24a)}
.book-cover.two{background:linear-gradient(#1d1d1d,#a61f1f)}
.book-cover.three{background:linear-gradient(#f4f4f4,#5aa24a)}
.btn-copy{background:var(--green);font-size:6.5px;padding:3px 8px;margin-top:-6px;position:relative}

/* what we do */
.services{height:170px;background:var(--blue);position:relative;padding-top:8px}
.services h2{text-align:center;color:#fff;font-size:14px;font-weight:600;margin-bottom:8px}
.services-panel{margin:0 70px;height:110px;background:#fff;display:flex;gap:14px;padding:12px 14px}
.service-tabs{width:150px}
.service-tabs li{background:var(--green);color:#fff;font-size:8.5px;font-weight:600;padding:5px 8px;margin-bottom:3px}
.service-tabs li.active{background:var(--green-dark)}
.service-cards{flex:1;display:flex;gap:8px}
.service-card{flex:1;text-align:center}
.service-photo{height:60px;background:linear-gradient(#9cc0e2,#c6b295 60%,#6e8f45)}
.service-card span{display:block;font-size:6.5px;font-weight:700;margin-top:4px}
.services-edge{position:absolute;left:0;right:0;bottom:-22px;height:30px}

/* testimonials & news */
.community{height:150px;display:flex;gap:24px;padding:34px 74px 0}
.testimonial{flex:1.1}
.testimonial-body{display:flex;gap:10px;margin-top:6px}
.portrait{flex:none;width:38px;height:38px;border-radius:50%;background:linear-gradient(#8aa0b3,#3e4a58);margin:0 auto}
.testimonial blockquote{font-size:6.8px;color:var(--muted);font-style:normal}
.author{font-size:7px;font-weight:700;margin-top:3px;width:56px;text-align:center;white-space:nowrap}
.news{flex:1}
.news li{display:flex;gap:8px;margin-top:7px}
.news-icon{flex:none;width:18px;height:18px;background:var(--blue)}
.news li:nth-child(2) .news-icon{background:var(--green)}
.news h4{font-size:7px;font-weight:700}
.news p{font-size:6.3px;color:var(--muted)}

/* call bar */
.callout{height:90px;position:relative;padding:16px 74px 0;overflow:hidden}
.callout-row{display:flex;align-items:flex-end;gap:14px}
.callout small{display:block;font-size:8px;color:var(--green);font-weight:700}
.callout strong{display:block;font-size:17px;font-weight:800;line-height:1.2;white-space:nowrap}
.btn-consult{background:var(--green);font-size:7.5px;padding:3px 10px 4px;text-transform:uppercase;text-align:center;line-height:1.2;margin-bottom:3px}
.btn-consult span{display:block;font-size:6px;font-weight:600;text-transform:none}
.callout-brand{position:absolute;right:86px;top:22px;font-size:22px;font-weight:800;color:var(--blue);opacity:.25}
.callout svg{position:absolute;left:0;bottom:0}

/* footer */
.site-footer{height:175px;background:var(--footer);color:#cfd2d6;display:flex;gap:22px;padding:18px 74px 0}
.site-footer h5{color:#fff;font-size:8.5px;font-weight:700;margin-bottom:8px}
.site-footer li{font-size:7px;margin-bottom:5px;display:flex;align-items:center;gap:5px}
.quick{width:80px}
.contact{width:130px}
.newsletter{width:120px}
.follow{flex:1}
.bullet{width:4px;height:4px;background:var(--green)}
.circle{width:11px;height:11px;border-radius:50%;background:var(--blue)}
.newsletter p{font-size:6.8px;margin-bottom:6px}
.field{height:14px;background:#fff;font-size:6.5px;color:#888;padding:2px 4px;margin-bottom:5px}
.btn-sub{background:var(--green);font-size:6.5px;padding:3px 8px}
.legal{height:20px;background:var(--footer-deep);color:#9aa0a6;font-size:6.5px;text-align:center;line-height:20px}
</style>
</head>
<body>

<header class="site-header">
  <div class="brand"><span class="brand-mark"></span>Loftvane</div>
  <div class="topbar">
    <div class="flag" role="img" aria-label="Canadian flag"><span></span><span></span><span></span></div>
    <span class="phone-dot"><svg width="8" height="8" viewBox="0 0 24 24"><path fill="#fff" d="M6.6 10.8a15 15 0 0 0 6.6 6.6l2.2-2.2c.3-.3.7-.4 1-.2 1.1.4 2.3.6 3.6.6.6 0 1 .4 1 1V20c0 .6-.4 1-1 1A17 17 0 0 1 3 4c0-.6.4-1 1-1h3.5c.6 0 1 .4 1 1 0 1.3.2 2.5.6 3.6.1.3 0 .7-.2 1z"/></svg></span>
    123-456-7890
  </div>
  <nav class="main-nav">
    <a class="active" href="#">Home</a><a href="#">Application</a><a href="#">Resource</a><a href="#">Calculator</a><a href="#">Contact Us</a>
  </nav>
</header>

<section class="hero" role="img" aria-label="Young couple standing at the front door of a new home">
  <div class="hero-caption">
    <h1>Customize Your Mortgages And Learn How To Save Thousands Of Dollars On Your Current Or Next Mortgage</h1>
    <a class="btn btn-start" href="#">Get Started</a>
  </div>
  <div class="slider-dots"><i></i><i></i><i></i></div>
</section>

<section class="features">
  <div class="feature">
    <span class="feature-icon"><svg width="14" height="14" viewBox="0 0 24 24"><path fill="none" stroke="#fff" stroke-width="3" d="M4 12l5 5 11-11"/></svg></span>
    <div><h3>Apply Online Now</h3><p>We work with the best lenders to find you a rate that fits your needs today.</p></div>
  </div>
  <div class="feature highlight">
    <span class="feature-icon"><svg width="14" height="14" viewBox="0 0 24 24"><rect x="3" y="6" width="18" height="13" fill="none" stroke="#56a532" stroke-width="2.5"/><circle cx="12" cy="12.5" r="3" fill="#56a532"/></svg></span>
    <div><h3>Save Thousands</h3><p>Customize your mortgage to fit your financial needs.</p></div>
  </div>
  <div class="feature">
    <span class="feature-icon"><svg width="14" height="14" viewBox="0 0 24 24"><rect x="5" y="3" width="14" height="18" fill="none" stroke="#fff" stroke-width="2.5"/><path d="M8 8h8M8 13h2M14 13h2M8 17h2M14 17h2" stroke="#fff" stroke-width="2"/></svg></span>
    <div><h3>Mortgage Calculator</h3><p>Customize your mortgage to fit your financial needs.</p></div>
  </div>
</section>

<section class="intro">
  <div class="welcome">
    <h2 class="section-title">Welcome To</h2>
    <div class="section-sub">Who are a Mortgage Broker?</div>
    <p>Professional representation for you and your family to help negotiate one of your biggest investments in your life. Helping you plan your mortgage to save over the next years.</p>
    <p class="access">24/7 Access</p>
    <a class="btn btn-more" href="#">Read More</a>
  </div>
  <div class="books">
    <h2 class="section-title">My Books</h2>
    <div class="section-sub">Please Read My Books</div>
    <div class="book-row">
      <div class="book"><div class="book-cover one" role="img" aria-label="Cover of first time home buyers resource guide"></div><a class="btn btn-copy" href="#">Free Copy</a></div>
      <div class="book"><div class="book-cover two" role="img" aria-label="Cover of mortgage savings book"></div><a class="btn btn-copy" href="#">Free Copy</a></div>
      <div class="book"><div class="book-cover three" role="img" aria-label="Cover of home financing book"></div><a class="btn btn-copy" href="#">Free Copy</a></div>
    </div>
  </div>
</section>

<section class="services">
  <h2>What We Do</h2>
  <div class="services-panel">
    <ul class="service-tabs">
      <li class="active">First Time Home Buyers</li>
      <li>Refinance Options</li>
      <li>Second Home</li>
      <li>New Purchase</li>
    </ul>
    <div class="service-cards">
      <div class="service-card"><div class="service-photo" role="img" aria-label="Suburban family home"></div><span>LOREM DOLLAR AM</span></div>
      <div class="service-card"><div class="service-photo" role="img" aria-label="Modern house exterior"></div><span>LOREM DOLLAR AM</span></div>
      <div class="service-card"><div class="service-photo" role="img" aria-label="Two-storey home with lawn"></div><span>LOREM DOLLAR AM</span></div>
    </div>
  </div>
  <svg class="services-edge" viewBox="0 0 684 30" preserveAspectRatio="none"><path d="M0 8 Q342 34 684 8 L684 0 L0 0Z" fill="#3277b5"/><path d="M0 8 Q342 34 684 8" fill="none" stroke="#56a532" stroke-width="4"/></svg>
</section>

<section class="community">
  <div class="testimonial">
    <h2 class="section-title">What Our Customers Speak</h2>
    <div class="testimonial-body">
      <div><div class="portrait" role="img" aria-label="Portrait of a client"></div><div class="author">Dana Whitfield</div></div>
      <blockquote>“Lorem ipsum dolor sit amet, consectetur adipiscing elit. Integer nec odio praesent libero sed cursus ante dapibus diam, sed nisi nulla quis sem at nibh elementum imperdiet duis sagittis ipsum mauris.”</blockquote>
    </div>
  </div>
  <div class="news">
    <h2 class="section-title">Recent News</h2>
    <ul>
      <li><span class="news-icon"></span><div><h4>Lorem ipsum dolor sit amet</h4><p>Consectetur adipiscing elit, nulla et nisi auctor sed.</p></div></li>
      <li><span class="news-icon"></span><div><h4>Lorem ipsum dolor sit amet</h4><p>Consectetur adipiscing elit, nulla et nisi auctor sed.</p></div></li>
      <li><span class="news-icon"></span><div><h4>Lorem ipsum dolor sit amet</h4><p>Consectetur adipiscing elit, nulla et nisi auctor sed.</p></div></li>
    </ul>
  </div>
</section>

<section class="callout">
  <div class="callout-row">
    <div>
      <small>Got any help?</small>
      <strong>Call 123-456-7890</strong>
    </div>
    <a class="btn btn-consult" href="#"><span>Schedule a</span>Free Consultation</a>
  </div>
  <div class="callout-brand">Loftvane</div>
  <svg width="684" height="22" viewBox="0 0 684 22" preserveAspectRatio="none"><path d="M0 22 Q300 0 684 14 L684 22Z" fill="#56a532"/><path d="M0 22 Q340 8 684 20 L684 22Z" fill="#3277b5"/></svg>
</section>

<footer class="site-footer">
  <div class="quick">
    <h5>Quick Links</h5>
    <ul><li><span class="bullet"></span>Home</li><li><span class="bullet"></span>Application</li><li><span class="bullet"></span>Resource</li><li><span class="bullet"></span>Calculator</li><li><span class="bullet"></span>Contact Us</li></ul>
  </div>
  <div class="contact">
    <h5>Contact Information</h5>
    <ul><li><span class="circle"></span>Loftvane Mortgages</li><li><span class="circle"></span>220 Harbour Street, Toronto ON</li><li><span class="circle"></span>123-456-7890</li><li><span class="circle"></span>www.loftvane.ca</li></ul>
  </div>
  <div class="newsletter">
    <h5>Newsletter Sign Up</h5>
    <p>Get mortgage tips and news delivered to your inbox.</p>
    <div class="field">Email Address</div>
    <a class="btn btn-sub" href="#">Subscribe</a>
  </div>
  <div class="follow">
    <h5>Follow Us</h5>
    <ul><li><span class="circle"></span>Newsfeed</li><li><span class="circle"></span>Updates</li><li><span class="circle"></span>Network</li><li><span class="circle"></span>Circles</li></ul>
  </div>
</footer>
<div class="legal">© 2024 Loftvane.ca. All Rights Reserved.</div>

</body>
</html>
```